依頼概要
■ 依頼の目的/概要

地域ポータルサイト、リニューアルのため、
手配り用のフライヤーデザインを募集。

■ 重視する点

オシャレなイメージを出したい。
A6サイズという小さなものなので、
載せられる情報量が限定されるが、
そこを上手にカバーしてもらいたい。

■ 納品

イラストレーター形式での納品希望

■ウェブサイト

みずたま Mizutama
http://www.mizutama-town.example/

http://www.mizutama-town.example/mizutama/magazine/01_01.cfm
(仮のページです。イメージだけご覧下さい)

■記載内容

・グルメ、美容など生活に密着した情報を
PCと携帯サイトで提供している

・オシャレにリニューアルした

・ポイントシステムを導入した。
毎日スロットができるほかに、口コミや
ストリートスナップを送るとポイントをゲットできる。
貯めたポイントは商品に交換できる。

・映画のチケットプレゼントなどお得な情報がいっぱい

以上のようなことを簡単に記載しておいてください。
詳細については、こちらでアレンジします。

■ロゴ

ロゴを添付します。
他にも必要な事項がありましたら、
おっしゃってください。

依頼公開後の追記内容
上記の仮ページURLが間違っておりました。

http://www.mizutama-town.example/~mizutama/magazine/01_01.cfm
ロゴを添付します
さっそくのご提案ありがとうございます。

【QRコード】
フライヤーに携帯QRコードを載せていただきますよう
お願いいたします。
■ 選んだ理由

オシャレに、というこちらの希望をうまく取り入れていただいたと思っています。
写真の女性が美しいというのも、好印象でした。

■ 提案者全員へのお礼・コメント

この度は、私どもの依頼にご提案いただきありがとうございました。

ぜひまた機会がありましたら、どうぞ宜しくお願いいたします。

```html
<!DOCTYPE html>
<html lang="ja">
<head>
<meta charset="utf-8">
<title>Mizutama Renewal Open</title>
<link rel="stylesheet" href="https://fonts.googleapis.com/css2?family=Noto+Sans+JP:wght@400;700;900&family=Playfair+Display:wght@400;700&display=swap">
<style>
  :root {
    --brown-dark: #4a2a1c;
    --brown: #6b3a26;
    --brick: #a8412f;
    --brick-light: #c0553f;
    --cream: #f4ede0;
    --pink: #e07a8c;
    --pink-text: #d23c6a;
    --ink: #3a2a22;
    --white: #ffffff;
  }
  * { margin: 0; padding: 0; box-sizing: border-box; }
  html, body { width: 851px; height: 1200px; overflow: hidden; background: var(--cream); }
  .flyer {
    position: relative; width: 851px; height: 1200px; overflow: hidden;
    background: var(--cream); font-family: "Noto Sans JP", sans-serif; color: var(--ink);
  }
  .category-strip {
    position: absolute; top: 0; left: 0; width: 100%; height: 24px;
    background: var(--brown-dark); color: var(--white);
    font-size: 12.5px; line-height: 24px; text-align: center; letter-spacing: 0.02em;
  }
  .tagline {
    position: absolute; top: 24px; left: 0; width: 100%; height: 62px;
    background: linear-gradient(#b04a34, var(--brick));
    color: var(--white); font-weight: 900; font-size: 37px; line-height: 62px;
    text-align: center; letter-spacing: 0.02em;
  }
  .hero-photo {
    position: absolute; top: 86px; left: 0; width: 100%; height: 298px;
    background: linear-gradient(100deg, #d8a86a 0%, #e9d4b2 35%, #efe6da 55%, #c7a89a 78%, #8e3a3c 100%);
  }
  .brand-name {
    position: absolute; top: 168px; left: 0; width: 100%; text-align: center;
    color: var(--white); font-size: 96px; font-weight: 700; letter-spacing: 0.02em; line-height: 1;
  }
  .renewal-band {
    position: absolute; top: 384px; left: 0; width: 100%; height: 184px;
    background: var(--brick);
    border-top: 4px solid var(--brown); border-bottom: 4px solid var(--brown);
  }
  .renewal-title {
    position: absolute; left: 70px; font-family: "Playfair Display", serif;
    color: var(--white); font-weight: 400; line-height: 1; letter-spacing: 0.03em;
  }
  .renewal-title.first { top: 400px; font-size: 88px; }
  .renewal-title.second { top: 482px; left: 170px; font-size: 88px; letter-spacing: 0.12em; }
  .date-badge {
    position: absolute; top: 412px; left: 700px; width: 104px; height: 104px; border-radius: 50%;
    background: var(--white); color: var(--brick);
    font-family: "Playfair Display", serif; font-weight: 700; font-size: 44px;
    display: flex; align-items: center; justify-content: center;
  }
  .model-photo {
    position: absolute; top: 568px; left: 520px; width: 331px; height: 565px;
    background: linear-gradient(180deg, #efe7dc 0%, #d9c9b8 45%, #bfa792 100%);
  }
  .lead {
    position: absolute; top: 578px; left: 40px; font-size: 22px; font-weight: 700; color: var(--ink);
  }
  .headline-box {
    position: absolute; top: 632px; left: 52px; width: 480px; height: 112px;
    background: var(--white); border: 4px solid var(--pink); border-radius: 6px;
    padding: 10px 18px; color: var(--pink-text); font-weight: 900;
  }
  .headline-box .row1 { font-size: 30px; line-height: 44px; }
  .headline-box .row1 .brand { font-size: 32px; margin-left: 8px; }
  .headline-box .row2 { font-size: 30px; line-height: 46px; }
  .points { position: absolute; top: 764px; left: 46px; width: 470px; list-style: none; }
  .points li {
    position: relative; padding-left: 26px; margin-bottom: 12px;
    font-size: 18.5px; line-height: 1.45; font-weight: 700; color: var(--ink);
  }
  .points li::before {
    content: ""; position: absolute; left: 2px; top: 7px; width: 14px; height: 14px;
    border-radius: 50%; background: var(--brick-light);
  }
  .points em { font-style: normal; color: var(--pink-text); }
  .site-footer {
    position: absolute; bottom: 0; left: 0; width: 100%; height: 67px;
    background: var(--brown); color: var(--white);
    font-size: 24px; font-weight: 700; line-height: 67px; text-align: center; letter-spacing: 0.03em;
  }
</style>
</head>
<body>
<div class="flyer">
  <div class="category-strip">観光・旅行・温泉・ホテル・宿泊・クーポン・レストラン・カフェ・ショッピング・アウトレット・不動産・ペット検索</div>
  <div class="tagline">満足感をUPしてオシャレにCHANGE!</div>

  <div class="hero-photo" role="img" aria-label="フルーツタルトと口紅・コスメのライフスタイル写真"></div>
  <div class="brand-name">Mizutama</div>

  <div class="renewal-band" role="img" aria-label="赤茶色の水玉模様の帯"></div>
  <div class="renewal-title first">RENEWAL</div>
  <div class="renewal-title second">OPEN</div>
  <div class="date-badge">9/1</div>

  <div class="model-photo" role="img" aria-label="携帯電話を持って微笑む女性の写真"></div>

  <p class="lead">名張・伊賀Lifeをゆたかにするwebマガジン</p>

  <div class="headline-box">
    <div class="row1">【みずたま】が<span class="brand">Mizutama</span></div>
    <div class="row2">として、生まれ変わります!!</div>
  </div>

  <ul class="points">
    <li>グルメ、美容など生活に密着した情報を<br>PCと携帯サイトで<em>提供中!</em></li>
    <li><em>ポイントシステムを導入しました。</em><br>毎日スロットができるほかに、<br>口コミやストリートスナップを送るとポイントをゲット!!<br>また、貯めたポイントは商品に交換できます。</li>
    <li>映画のチケットプレゼントなどお得な情報がいっぱい!</li>
  </ul>

  <div class="site-footer">http://www.mizutama-town.example/</div>
</div>
</body>
</html>
```